Small Business Directory Site Requires a Professional Responsive Web Design

Small Business Directory and Coupon Site - we require a complete website design for a brand new responsive & mobile friendly website. We already have a coder who will professional code our website in Magento.

All PSD pages need to be professionally designed then uploaded into a sharedrive (i.e. like dropbox). Additionally, as I cannot pre-empt everything, please note that we may require a little more assistance once the files have been transferred (for example, in www.brindlestack.com if you hover your mouse on the search box you will see a pop up box. We want one of these too and I think that means there may be extra design work here)

We have some draft page sketches have been created (there are some minor changes we want to the sketches provided though); however, we require an excellent designer to add the creative touches to it to make it look professionally created. All artwork/font must be legal.

-------------------------
We like the look of the www.brindlestack.com and www. quorvanet.com

For the headers, please consider a font similar to RNS camellia. We likes this style, but it is too thin for the headers...so we need a variation like this one. For the copy/general text font, something basic that marries well with the headers.

---------------------

Please be sure to also read the brief we wrote for the coder as this will help with better understanding our design requirements.

In total I believe we have about 50 pages. This includes all the little pages and most of the pop up boxes (but not the little help key boxes). For example, pages include...

1. Login (this is where customers log in and can edit, manage their profiles. This means that there are backend membership pages)
2. Mini Services (same look and feel as the business coupons)
3. Resource Centre
4. Join (this is where customers learn about the packages available to submit a directory listing, if they ‘buy’ a package (i.e. free, $25 or $150 package) then they can create their own directory listing)
5. Search the directory (customer can view all the categories and also search the directory)
6. Create a directory listing (this is where customers learn about the packages available to submit a directory listing, if they ‘buy’ a package (i.e. free, $25 or $150 package) then they can create their own directory listing)
7. Quote finder (also know as Get a Quote)
8. Coupons (customer go to the business coupon page and can view all current coupons/submit a coupon)
9. Submit a coupon (form)
10.Advertise with us (form)
11. Join the forum
12.Submit an article or video (form)
13. Affiliates (listing of affiliates we currently have)
14. Become an affiliate (form)
15. Case studies (customer can view the case studies we have in the resource centre)
16. Help Guides (customer can view the help guides we have in the resource centre)
17. About Us
18 .Contact Us (form)
19. Terms & Condition
20. Privacy Policy
21. Supporting City Councils
22. Site Map
23. Forgot password / login details
24. Homepage
25. If we hover over a few areas (i.e. search box, location field) it pops up with more information.
etc etc etc. . . there are more pages.

Please see our dropbox link for the draft mock up pages that I have created so far.

https://www.filmorrow.com/sh/kq82pl4vmd7wtz/QZtrXnBeLopVacd3Ju7fGhWkS

We are in a rush! We'd like to get the majority of the artwork completed by the end of the month. Minor fixes/tweaks can occur thereafter.

Target Market(s)

Small Businesses (employees 0 - 50) located throughout Australia

Industry/Entity Type

Business

Font styles to use
Sans Serif

Requirements
Must have
• Professional. Artwork must be legal (cannot be cut and paste or taken off other websites, must be legally purchased and used).Must look contemporary, fresh, modern.

Absolutely must be a responsive site!
Nice to have
• original work, original photos, original art.

like modern, fresh photos that demonstrate innovation, growth, small business, Australian scenery, stability, goals/passion.
Should not have
• cut and paste graphics, illegal graphics, not purchased graphics.

```html
<!DOCTYPE html>
<html lang="en">
<head>
<meta charset="utf-8">
<title>Kestrel Biz Link — Home</title>
<link href="https://fonts.googleapis.com/css2?family=Lato:wght@400;700&family=Quicksand:wght@400;500;600&display=swap" rel="stylesheet">
<style>
:root{
  --orange:#f07d12;
  --orange-dark:#d9660a;
  --ink:#333;
  --muted:#6b6b6b;
  --line:#dcdcdc;
  --bar:#1c1c1c;
  --footer:#050505;
  --footer-bottom:#2b2b2b;
  --white:#fff;
}
*{box-sizing:border-box;margin:0;padding:0}
html,body{width:778px;height:1200px;overflow:hidden;background:var(--white)}
body{position:relative;font-family:"Lato",Arial,sans-serif;color:var(--ink)}
.abs{position:absolute}
a{color:inherit;text-decoration:none}

/* header */
.site-header{top:0;left:0;width:778px;height:70px}
.brand{left:84px;top:18px;display:flex;align-items:center;gap:8px}
.brand-mark{width:26px;height:26px;border-radius:4px;background:var(--orange)}
.brand-name{font-family:"Quicksand",sans-serif;font-weight:600;font-size:17px;color:var(--ink)}
.main-nav{left:286px;top:29px;display:flex;font-size:10px;color:var(--ink)}
.main-nav a{padding:0 8px;border-left:1px solid var(--line);line-height:13px}
.main-nav a:first-child{border-left:none}

/* hero */
.hero{top:70px;left:0;width:778px;height:303px;
  background:linear-gradient(180deg,#8a9aa6 0%,#d9a03f 22%,#f29a1a 42%,#e88a10 60%,#f4a21f 78%,#c8720c 100%)}
.hero-title{left:84px;top:88px;font-family:"Quicksand",sans-serif;font-size:25px;font-weight:500;color:var(--white)}
.hero-sub{left:84px;top:120px;font-family:"Quicksand",sans-serif;font-size:14px;color:var(--white)}
.search-bar{left:88px;top:145px;width:360px;height:35px;background:var(--orange);display:flex;align-items:center;gap:5px;padding:0 8px}
.search-bar .field{height:20px;background:var(--white);font-size:7.5px;color:#999;padding:6px 8px}
.search-bar .what{width:134px}.search-bar .where{width:115px}
.search-bar .go{width:24px;height:20px;background:#111;display:flex;align-items:center;justify-content:center}
.search-bar .join{height:20px;background:#111;color:var(--white);font-weight:700;font-size:9.5px;padding:4px 10px}
.services-card{left:514px;top:45px;width:182px;height:210px;background:rgba(90,90,90,.55);color:var(--white);text-align:center}
.services-card h3{font-family:"Quicksand",sans-serif;font-weight:500;font-size:17px;margin-top:14px}
.services-card .lead{font-size:8.5px;margin-top:2px}
.services-card .shot{position:absolute;left:38px;top:57px;width:108px;height:72px;background:linear-gradient(135deg,#4b6a8a,#b9c9d8);border:3px solid #ddd}
.services-card .arrow{position:absolute;top:90px}
.services-card .tag{position:absolute;left:16px;top:147px;font-size:7.5px;color:var(--orange);font-weight:700}
.services-card .desc{position:absolute;left:16px;top:159px;font-size:6.5px;text-align:left}
.services-card .price{position:absolute;left:17px;top:176px;font-family:"Quicksand",sans-serif;font-size:13px}
.services-card .price small{font-size:7px}
.services-card .cta{position:absolute;left:93px;top:177px;width:64px;height:17px;background:var(--orange);font-size:7px;line-height:17px;border-radius:2px}
.hero-dots{left:369px;top:288px;display:flex;gap:3px}
.hero-dots span{width:8px;height:8px;border-radius:50%;background:var(--white)}

/* category bar */
.category-bar{top:373px;left:0;width:778px;height:27px;background:var(--bar);display:flex;justify-content:center}
.category-bar a{color:var(--white);font-size:7.5px;line-height:27px;padding:0 5px;border-left:1px solid #444}
.category-bar a:first-child{border-left:none}
.category-bar a.all{background:var(--orange)}

/* community */
.section-title{left:0;width:778px;text-align:center;font-family:"Quicksand",sans-serif;font-weight:500;color:var(--ink)}
.community-title{top:420px;font-size:20px}
.feature{top:465px;width:190px;text-align:center}
.feature h4{font-family:"Quicksand",sans-serif;font-weight:500;color:var(--orange);font-size:13.5px;line-height:18px;height:40px;display:flex;align-items:center;justify-content:center}
.feature .media{width:185px;height:104px;margin:4px auto 0;border:1px solid var(--line)}
.feature p{font-size:7.5px;color:var(--muted);line-height:13px;margin:6px auto 0;width:185px}
.btn{display:inline-block;background:var(--orange);color:var(--white);font-size:8px;padding:6px 14px;border-radius:2px;margin-top:14px;border-bottom:2px solid var(--orange-dark)}
.partner-box{display:flex;align-items:center;justify-content:center;gap:8px;font-family:"Quicksand",sans-serif;font-weight:600;font-size:14px;color:#1f4c8a;height:97px!important;margin-top:7px!important}
.partner-box i{width:20px;height:20px;border-radius:50%;background:#1f4c8a}
.divider{top:746px;left:83px;width:613px;height:1px;background:var(--line)}

/* coupons */
.coupons-title{top:764px;font-size:15px}
.coupon{top:798px;width:129px;height:122px;border:1px solid var(--line);text-align:center}
.coupon .art{width:88px;height:48px;margin:17px auto 0}
.coupon h5{font-family:"Quicksand",sans-serif;font-weight:500;font-size:9.5px;color:var(--orange);margin-top:7px}
.coupon p{font-size:7px;color:var(--muted);margin-top:2px}
.coupon .amount{font-family:"Quicksand",sans-serif;font-size:12px;margin-top:5px;color:#222}

/* partner strip */
.partner-strip{top:944px;left:0;width:778px;height:48px;background:#f4f4f4;display:flex;justify-content:center;gap:90px;align-items:center}
.partner-strip span{font-family:"Quicksand",sans-serif;font-weight:600;font-size:17px;color:#a9a9a9}

/* footer */
.site-footer{top:992px;left:0;width:778px;height:168px;background:var(--footer)}
.footer-col{top:1019px}
.footer-col h6{font-family:"Quicksand",sans-serif;font-weight:600;font-size:10px;color:var(--orange);margin-bottom:8px}
.footer-col li{list-style:none;font-size:7.5px;color:var(--white);line-height:14.2px}
.social{display:flex;gap:7px;margin-top:2px}
.social span{width:17px;height:15px;border-radius:2px;background:#3a6fb0}
.subscribe{display:inline-block;margin-top:18px;background:var(--orange);color:#111;font-size:7.5px;padding:5px 5px}
.footer-bottom{top:1160px;left:0;width:778px;height:40px;background:var(--footer-bottom);color:#7d7d7d;font-size:7.5px;padding:17px 0 0 90px}
</style>
</head>
<body>

<header class="site-header abs">
  <div class="brand abs"><span class="brand-mark"></span><span class="brand-name">Kestrel Biz Link</span></div>
  <nav class="main-nav abs">
    <a href="#">Login</a><a href="#">Join</a><a href="#">Coupons</a><a href="#">Mini Service</a><a href="#">Get a Quote</a><a href="#">Advertise</a><a href="#">Resource Centre</a>
  </nav>
</header>

<section class="hero abs" role="img" aria-label="Photo of an orange sunset over calm water with hills on the horizon">
  <h1 class="hero-title abs">It’s a Brand New Day.</h1>
  <p class="hero-sub abs">Do More of What Your Love</p>
  <form class="search-bar abs">
    <div class="field what">What are you looking for?</div>
    <div class="field where">Where?</div>
    <div class="go"><svg width="11" height="11" viewBox="0 0 12 12"><circle cx="5" cy="5" r="3.8" fill="none" stroke="#fff" stroke-width="1.6"/><line x1="8" y1="8" x2="11" y2="11" stroke="#fff" stroke-width="1.8"/></svg></div>
    <div class="join">Join Us</div>
  </form>
  <aside class="services-card abs">
    <h3>Our Services</h3>
    <p class="lead">Services which we provide</p>
    <svg class="arrow" style="left:13px" width="10" height="18" viewBox="0 0 10 18"><polyline points="8,1 2,9 8,17" fill="none" stroke="#fff" stroke-width="1.5"/></svg>
    <div class="shot" role="img" aria-label="Laptop screen showing a business problem-solving diagram"></div>
    <svg class="arrow" style="left:159px" width="10" height="18" viewBox="0 0 10 18"><polyline points="2,1 8,9 2,17" fill="none" stroke="#fff" stroke-width="1.5"/></svg>
    <div class="tag">3 CATEGORY LISTING</div>
    <div class="desc">Lorem ipsum dolor sit amet consectetuer adip</div>
    <div class="price">A $25/<small>YEAR</small></div>
    <div class="cta">CLICK HERE</div>
  </aside>
  <div class="hero-dots abs"><span></span><span></span><span></span><span></span></div>
</section>

<nav class="category-bar abs">
  <a href="#">Banking, Finance &amp; Insurance</a><a href="#">Marketing, Design, Photography, Video &amp; Print</a><a href="#">Coaching &amp; Training</a><a href="#">Technology</a><a href="#">Legal</a><a href="#">Administration</a><a href="#" class="all">View All Category</a>
</nav>

<h2 class="section-title community-title abs">Get Real Support from Our Community</h2>

<article class="feature abs" style="left:94px">
  <h4>How Did You Sort<br>Your Business?</h4>
  <div class="media" role="img" aria-label="Photo of a desk with a tablet, glasses and printed charts" style="background:linear-gradient(135deg,#e9eef3,#b8c7d6)"></div>
  <p>Text: Learn from Dana Morrow, a real small business owner. How she started her business and what are the valuable resources for her right now.</p>
  <a class="btn" href="#">CASE STUDY</a>
</article>

<article class="feature abs" style="left:305px">
  <h4>Why Go with<br>Kestrel Biz Link?</h4>
  <div class="media" role="img" aria-label="Video still of two business people talking over a laptop" style="background:linear-gradient(135deg,#d7dde3,#2d4f7c);position:relative">
    <svg style="position:absolute;left:79px;top:38px" width="28" height="28" viewBox="0 0 28 28"><circle cx="14" cy="14" r="13" fill="#fff"/><polygon points="11,8 20,14 11,20" fill="#222"/></svg>
  </div>
  <p>What small business owner can’t relate to the ongoing task of attracting new customers? Struggling with cash flow? Or how about not having enough time in the day? It’s obvious that small businesses suffer from a lack of support. And that’s where we come in</p>
  <a class="btn" href="#" style="margin-top:8px">WHITEBOARD VIDEO</a>
</article>

<article class="feature abs" style="left:514px">
  <h4>Become an Affiliate</h4>
  <div class="media partner-box"><i></i>Harbourline Cover</div>
  <p>If you have a network of small businesses, let us help to create additional value for your members and make money for your network. Talk to us today about how we can help.</p>
</article>

<div class="divider abs"></div>

<h2 class="section-title coupons-title abs">Featured Business Coupons</h2>

<div class="coupon abs" style="left:115px"><div class="art" role="img" aria-label="Green banknote-style coupon artwork" style="background:linear-gradient(#cfe0c2,#8fb07a)"></div><h5>Coupon Tittle</h5><p>Lorem ipsum dolor sit amet</p><div class="amount">$3,000</div></div>
<div class="coupon abs" style="left:254px"><div class="art" role="img" aria-label="Cream breakfast coupon with red trim" style="background:linear-gradient(#fbf4e4,#e7d6b4);border:2px solid #2f6b3a"></div><h5>Coupon Tittle</h5><p>Lorem ipsum dolor sit amet</p><div class="amount">$3,000</div></div>
<div class="coupon abs" style="left:392px"><div class="art" role="img" aria-label="Teal cupcake shop discount coupon" style="background:linear-gradient(#7fc9c6,#f3dca0)"></div><h5>Coupon Tittle</h5><p>Lorem ipsum dolor sit amet</p><div class="amount">$3,000</div></div>
<div class="coupon abs" style="left:531px"><div class="art" role="img" aria-label="White shopping bag discount coupon" style="background:linear-gradient(#ffffff,#e6e6e6);border:1px solid #ddd"></div><h5>Coupon Tittle</h5><p>Lorem ipsum dolor sit amet</p><div class="amount">$3,000</div></div>

<div class="partner-strip abs"><span>Vantora</span><span>Pelloform</span><span>Quillway</span></div>

<footer class="site-footer abs"></footer>
<div class="footer-col abs" style="left:84px"><h6>SITE DIRECTORY</h6><ul><li>Search the Directory</li><li>Create a Directory Listing</li><li>Quote Finder</li><li>Coupons</li><li>Submit A Coupon</li><li>Advertise with us</li></ul></div>
<div class="footer-col abs" style="left:203px"><h6>SITE DIRECTORY</h6><ul><li>Join the Forum</li><li>Submit an Article or Video</li><li>Affiliates</li><li>Become an Affiliate</li><li>Case Studies</li><li>Help Guides</li></ul></div>
<div class="footer-col abs" style="left:325px"><h6>POPULAR CATEGORIES</h6><ul><li>Etiam est nunc</li><li>Venenatis tristique</li><li>Emperdiet ac nisl</li><li>Cum sociis natoque</li><li>Penatibus et magnis</li></ul></div>
<div class="footer-col abs" style="left:458px"><h6>ABOUT</h6><ul><li>About Us</li><li>Contact Us</li><li>Term &amp; Conditions</li><li>Privacy Policy</li><li>Supporting City Councils</li><li>Site Map</li></ul></div>
<div class="footer-col abs" style="left:570px"><h6>FOLLOW US</h6><div class="social"><span style="background:#c9302c"></span><span></span><span style="background:#4aa3df"></span><span style="background:#2a6ea8"></span></div><a class="subscribe" href="#">Subscribe to our Coupon Deals</a></div>

<div class="footer-bottom abs">© 2014 Company Name&nbsp; All right reserved&nbsp; Term of Use</div>

</body>
</html>
```